Dermavale "polish what the seasons left you" The whole body approach to beauty, customized skincare a

I need a stronger logo design than what I have now. I currently have a small med spa in Chicago, IL. I will be expanding my brand to New York City and the Hamptons of NY. The services I provide in Chicago include; advanced medical grade skincare treatments, laser, plastic surgery and nutrition counsel. My concept is personalized skincare. Part of my philosophy is to dedicate a lot of time and make myself always available to my clients questions and concerns. To maintain integrity of the Dermavale Philosophy I do not advertise. Dermavale is an "exclusive skincare club" therefore you must be referred by an existing client or staff member in order to get an appointment. My Chicago clientele consists of young professionals competing with their peers to look their absolute best. The New York and Hamptons business has a completely different structure. It is a Mobile med spa service providing treatments at people's homes. The services provided are advanced skincare, wellness, massage, spray tan, hair and makeup. My vision for the new logo design is to exude an image that is both cutting edge, relevant, sophisticated, sexy and modern (sleek) yet practical and strong. It must be eye catching yet simplistic, aesthetically pleasing to look at and above all must promote EXCLUSIVITY! bellow I have attached my current logo design which is printed using silver and gold foil. The other is the logo on my prescription skincare products. I need to merge the two for the brand to be cohesive. I would like to print my business cards on a mirror like material where you can see your reflection. Front of card: the brand Dermavale across the front and across the bottom will be Chicago. New York. Hamptons Back of card: in a font style like writing "Dermavale is the whole body approach to beauty. customized medical grade skincare. massage. wellness counsel. By appointment only
www.dermavalewellness-example.com p: (555) 318-2406
I am open to all suggestions to make my brand as strong as possible. Please be creative and relevant. Thank you!

```html
<!DOCTYPE html>
<html lang="en">
<head>
<meta charset="utf-8">
<title>Dermavale Business Card</title>
<link rel="stylesheet" href="https://fonts.googleapis.com/css2?family=Cormorant+Garamond:wght@500&family=Raleway:wght@300;400&family=Lato:ital,wght@1,400&display=swap">
<style>
  :root {
    --backdrop: #e6e6e6;
    --card: #ffffff;
    --gold-light: #f1dd72;
    --gold: #c9a136;
    --gold-deep: #a97d22;
    --ink: #6f6f6f;
    --ink-soft: #8d8d8d;
  }
  * { box-sizing: border-box; margin: 0; padding: 0; }
  html, body { width: 1200px; height: 900px; overflow: hidden; }
  body {
    background: var(--backdrop);
    display: flex;
    align-items: center;
    justify-content: center;
    gap: 60px;
  }
  .card {
    position: relative;
    width: 510px;
    height: 310px;
    background: var(--card);
    border-radius: 22px;
    box-shadow: 0 6px 18px rgba(0,0,0,0.12);
  }
  .card__frame {
    position: absolute;
    inset: 9px;
    border-radius: 16px;
    border: 8px solid var(--gold);
    border-image: none;
    background:
      linear-gradient(var(--card), var(--card)) padding-box,
      linear-gradient(100deg, var(--gold-deep), var(--gold-light) 45%, var(--gold) 70%, var(--gold-deep)) border-box;
    border-color: transparent;
  }
  .card__content {
    position: absolute;
    inset: 17px;
    display: flex;
    flex-direction: column;
    align-items: center;
    text-align: center;
  }
  .brand-name {
    font-family: "Cormorant Garamond", serif;
    font-weight: 500;
    color: var(--gold);
    text-transform: uppercase;
    line-height: 1;
  }
  .tagline {
    font-family: "Raleway", sans-serif;
    font-weight: 300;
    color: var(--ink-soft);
    letter-spacing: 0.32em;
  }
  /* front */
  .card--front .brand-name { font-size: 64px; letter-spacing: 0.02em; margin-top: 84px; }
  .card--front .tagline { font-size: 15px; margin-top: 6px; }
  .cities {
    position: absolute;
    left: 14px;
    bottom: 16px;
    font-family: "Cormorant Garamond", serif;
    font-weight: 500;
    font-size: 13px;
    letter-spacing: 0.55em;
    color: var(--ink);
    text-transform: uppercase;
  }
  /* back */
  .card--back .brand-name { font-size: 34px; margin-top: 38px; }
  .card--back .tagline { font-size: 8.5px; margin-top: 3px; letter-spacing: 0.3em; }
  .philosophy {
    font-family: "Lato", sans-serif;
    font-style: italic;
    font-size: 13px;
    line-height: 1.35;
    color: var(--ink);
    margin-top: 30px;
    letter-spacing: 0.03em;
  }
  .appointment {
    font-family: "Raleway", sans-serif;
    font-weight: 400;
    font-size: 9px;
    letter-spacing: 0.05em;
    color: var(--ink);
    margin-top: 24px;
  }
  .contact {
    font-family: "Raleway", sans-serif;
    color: var(--ink);
    margin-top: 12px;
    line-height: 1.3;
  }
  .contact__web { font-size: 11px; letter-spacing: 0.15em; }
  .contact__phone { font-family: "Cormorant Garamond", serif; font-weight: 500; font-size: 16px; letter-spacing: 0.18em; }
</style>
</head>
<body>
  <section class="card card--front">
    <div class="card__frame"></div>
    <div class="card__content">
      <h1 class="brand-name">Dermavale</h1>
      <p class="tagline">polish what the seasons left you</p>
      <p class="cities">Chicago. New York. Hamptons</p>
    </div>
  </section>

  <section class="card card--back">
    <div class="card__frame"></div>
    <div class="card__content">
      <h2 class="brand-name">Dermavale</h2>
      <p class="tagline">polish what the seasons left you</p>
      <p class="philosophy">Dermavale is the whole body approach to beauty.<br>customized medical grade skincare. massage. wellness counsel.</p>
      <p class="appointment">BY APPOINTMENT ONLY</p>
      <div class="contact">
        <p class="contact__web">www.dermavalewellness-example.com</p>
        <p class="contact__phone">(555) 318-2406</p>
      </div>
    </div>
  </section>
</body>
</html>
```